Discreet simple classy for adult entertainment

I would like a matte black business card with gold writing for my business. Keeping it simple. Having my following:

Lina frost
Events. Entertainment. Promotions
0477250618

or alternatively could have what i had on my previous card below but i think i prefer the above as again - discretion.

Maybe a nice gold line thru the card or some other very simple design . Or not open to ideas/ can be doublesided if any good ideas with that.

included pics of my old bus card. not sure weather i want a photo on it or not. if i do it wont be the same pic. i kinda wanted a card that was discreet so if it was in someones wallet they wouldn't neccessarily realise it was from a stripper.

Target Market(s)

men

Industry/Entity Type

Business

Contact Information for Business Card

Lina frost
0477250618

Requirements
Nice to have
• i don't know i am really open to anything. im giving my cards to guys so something they can have in their wallet that is discreet preferably.

```html
<!DOCTYPE html>
<html lang="en">
<head>
<meta charset="utf-8">
<title>Lina Frost – Business Card</title>
<link rel="stylesheet" href="https://fonts.googleapis.com/css2?family=Lato:wght@300;400&display=swap">
<style>
  :root {
    --page-bg: #ffffff;
    --card-black: #060504;
    --gold: #c9a15a;
    --gold-light: #e6c583;
    --glitter-warm: rgba(214, 170, 90, 0.55);
    --glitter-soft: rgba(150, 110, 50, 0.25);
  }
  * { margin: 0; padding: 0; box-sizing: border-box; }
  html, body {
    width: 1200px;
    height: 960px;
    overflow: hidden;
    background: var(--page-bg);
  }
  .canvas {
    position: relative;
    width: 1200px;
    height: 960px;
  }
  .business-card {
    position: absolute;
    left: 74px;
    top: 174px;
    width: 1052px;
    height: 604px;
    background: var(--card-black);
    overflow: hidden;
    font-family: "Lato", sans-serif;
  }
  .glitter-field {
    position: absolute;
    left: 0;
    right: 0;
    bottom: 0;
    height: 300px;
    background:
      radial-gradient(ellipse 60% 70% at 20% 100%, var(--glitter-warm), transparent 70%),
      radial-gradient(ellipse 55% 65% at 75% 100%, var(--glitter-warm), transparent 70%),
      linear-gradient(to bottom, transparent 0%, var(--glitter-soft) 55%, var(--glitter-warm) 100%);
  }
  .name {
    position: absolute;
    left: 118px;
    top: 118px;
    color: var(--gold);
    font-weight: 300;
    font-size: 152px;
    line-height: 142px;
    letter-spacing: 6px;
    text-transform: uppercase;
  }
  .divider {
    position: absolute;
    left: 630px;
    top: 120px;
    width: 2px;
    height: 272px;
    background: var(--gold);
  }
  .services {
    position: absolute;
    left: 670px;
    top: 136px;
    list-style: none;
    color: var(--gold-light);
    font-size: 36px;
    line-height: 54px;
    font-weight: 400;
  }
  .phone {
    position: absolute;
    left: 670px;
    top: 362px;
    color: var(--gold-light);
    font-size: 46px;
    font-weight: 400;
    letter-spacing: 1px;
  }
</style>
</head>
<body>
  <main class="canvas">
    <section class="business-card">
      <div class="glitter-field" role="img" aria-label="Scattered gold glitter sparkles rising from the bottom edge"></div>
      <h1 class="name">Lina<br>Frost</h1>
      <div class="divider"></div>
      <ul class="services">
        <li>Events</li>
        <li>Entertainment</li>
        <li>Promotions</li>
      </ul>
      <p class="phone">0477250618</p>
    </section>
  </main>
</body>
</html>
```